Looking for a modern website banner design

Corvella Fieldmark Consultants looking for the development of the main banner of the website. The project description and photos are included in the upload files.

```html
<!DOCTYPE html>
<html lang="en">
<head>
<meta charset="utf-8">
<title>Corvella Fieldmark Consultants – Athlete Testimonial Banner</title>
<link href="https://fonts.googleapis.com/css2?family=Roboto:wght@300;400;500;700&display=swap" rel="stylesheet">
<style>
  :root {
    --page: #ffffff;
    --panel-dark: #222222;
    --stripe-blue: #1f7fcf;
    --band-blue: #25a3dc;
    --text-light: #f2f2f2;
    --name-blue: #2aa3e2;
    --rule: #bdbdbd;
  }
  * { margin: 0; padding: 0; box-sizing: border-box; }
  html, body {
    width: 1200px; height: 600px; overflow: hidden;
    background: var(--page);
    font-family: "Roboto", Arial, sans-serif;
  }
  .banner {
    position: absolute; left: 76px; top: 58px;
    width: 1042px; height: 488px;
    background: var(--panel-dark);
    overflow: hidden;
  }
  .banner__art { position: absolute; inset: 0; width: 100%; height: 100%; }
  .testimonial {
    position: absolute; left: 39px; top: 72px; width: 520px;
    color: var(--text-light);
  }
  .testimonial__quote {
    font-weight: 300; font-size: 25.5px; line-height: 29.3px;
    white-space: nowrap;
  }
  .testimonial__quote strong { font-weight: 700; }
  .testimonial__rule {
    width: 72px; height: 3px; background: var(--rule);
    margin-top: 22px;
  }
  .athlete { margin-top: 18px; text-transform: uppercase; font-size: 17px; line-height: 22px; }
  .athlete__name { color: var(--name-blue); font-weight: 400; }
  .athlete__team, .athlete__league { color: var(--text-light); font-weight: 500; }
</style>
</head>
<body>
  <section class="banner">
    <svg class="banner__art" viewBox="0 0 1042 488" preserveAspectRatio="none">
      <defs>
        <linearGradient id="arena-tones" x1="0" y1="0" x2="0" y2="1">
          <stop offset="0" stop-color="#2b2a30"/>
          <stop offset="0.45" stop-color="#4a3a3c"/>
          <stop offset="0.7" stop-color="#b9b5b3"/>
          <stop offset="1" stop-color="#e9ecef"/>
        </linearGradient>
      </defs>

      <rect class="band-bottom" x="0" y="413" width="520" height="75" fill="var(--band-blue)"/>

      <polygon class="photo-area" role="img" aria-label="Photo of a hockey player celebrating a goal in front of a cheering arena crowd"
               points="702,0 1042,0 1042,488 407,488" fill="url(#arena-tones)"/>

      <polygon class="stripe stripe--main" points="666,0 702,0 407,488 350,488" fill="var(--stripe-blue)"/>
      <polygon class="stripe stripe--inner" points="575,282 602,282 458,488 430,488" fill="var(--stripe-blue)"/>
      <polygon class="stripe stripe--right-upper" points="1042,233 1042,270 913,444 890,444" fill="var(--stripe-blue)"/>
      <polygon class="stripe stripe--right-lower" points="904,488 984,488 1042,411 1042,298" fill="var(--stripe-blue)"/>
      <polygon class="corner-dark" points="984,488 1042,488 1042,411" fill="var(--panel-dark)"/>
    </svg>

    <div class="testimonial">
      <p class="testimonial__quote">“Corvella Fieldmark has provided support that<br>has allowed me to develop as a person and an<br>athlete.&nbsp; The <strong>S.T.R.I.D.E.™</strong> process allowed<br>me to stay focused on <strong>attainable goals</strong><br><strong>each season</strong> and <strong>progress from</strong><br><strong>Junior to College</strong> and now<br><strong>Professional Hockey</strong>.”</p>
      <div class="testimonial__rule"></div>
      <div class="athlete">
        <p class="athlete__name">Marcus Delane</p>
        <p class="athlete__team">Riverton Falcons</p>
        <p class="athlete__league">Atlantic Pro Hockey League</p>
      </div>
    </div>
  </section>
</body>
</html>
```